Criação de Papelaria (6 itens) para Automotivo
" Importamos automóveis premium como Vostrelli, Quintavessa, Dunholt sob encomenda. Importamos pecas de reposicao para veiculos premium "

```html
<!DOCTYPE html>
<html lang="pt-BR">
<head>
<meta charset="UTF-8">
<title>Veltra Importação — Pasta</title>
<link href="https://fonts.googleapis.com/css2?family=Montserrat:wght@700&family=Tinos&display=swap" rel="stylesheet">
<style>
  :root{
    --stage:#e9e6e1;
    --folder:#151413;
    --folder-edge:#0d0c0c;
    --folder-shade:#1c1b1a;
    --band:#2a2927;
    --gold:#d9be6a;
    --text:#b9b4aa;
  }
  *{margin:0;padding:0;box-sizing:border-box}
  html,body{width:1200px;height:1200px;overflow:hidden;background:var(--stage)}
  .spread{position:absolute;left:120px;top:210px;width:960px;height:780px;display:flex;box-shadow:0 18px 40px rgba(0,0,0,.25)}
  .panel{position:relative;width:480px;height:780px;background:var(--folder);overflow:hidden}
  .panel--back{border-right:1px solid var(--folder-edge)}
  .edge-line{position:absolute;left:0;right:0;height:2px;background:var(--gold)}
  .edge-line--top{top:8px}
  .edge-line--bottom{bottom:14px}
  .edge-accent{position:absolute;height:4px;background:var(--gold);bottom:13px}
  .contacts{position:absolute;left:36px;top:600px;width:420px;font-family:"Tinos",serif;font-size:11px;color:var(--text)}
  .contact-row{display:flex;align-items:center;height:26px}
  .contact-row .phones{width:170px}
  .contact-icon{width:16px;height:16px;margin-right:12px;flex:none}
  .address-band{position:absolute;left:0;right:0;top:690px;height:34px;background:var(--band);display:flex;align-items:center;padding-left:36px;font-family:"Tinos",serif;font-size:11px;color:var(--text)}
  .backdrop-shape{position:absolute;left:-120px;top:130px;width:400px;height:560px;border-radius:50%;background:var(--folder-shade)}
  .brand{position:absolute;left:80px;top:360px;display:flex;align-items:center}
  .brand-dot{width:36px;height:36px;border-radius:50%;background:var(--gold);margin-right:14px}
  .brand-name{font-family:"Montserrat",sans-serif;font-weight:700;font-size:44px;line-height:1;color:var(--gold);letter-spacing:1px}
</style>
</head>
<body>
  <div class="spread">
    <section class="panel panel--back">
      <div class="edge-line edge-line--top"></div>

      <div class="contacts">
        <div class="contact-row">
          <span class="phones">(00) 0000-0000 | (00) 00000-0000</span>
          <svg class="contact-icon" viewBox="0 0 16 16"><circle cx="8" cy="8" r="7.5" fill="none" stroke="var(--text)"/><path d="M5.5 4.5l1.5 0 .6 2-1 .8a5 5 0 0 0 2.1 2.1l.8-1 2 .6v1.5c-3.5.3-6.3-2.5-6-6z" fill="var(--text)"/></svg>
          <svg class="contact-icon" viewBox="0 0 16 16"><rect x="1" y="3.5" width="14" height="9" rx="1" fill="none" stroke="var(--text)"/><path d="M1.5 4l6.5 5 6.5-5" fill="none" stroke="var(--text)"/></svg>
          <span>contato@veltraimportacao.com.br</span>
        </div>
        <div class="contact-row">
          <span class="phones">(00) 0000-0000 | (00) 00000-0000</span>
          <svg class="contact-icon" viewBox="0 0 16 16"><circle cx="8" cy="8" r="7.5" fill="none" stroke="var(--text)"/></svg>
          <svg class="contact-icon" viewBox="0 0 16 16"><circle cx="8" cy="8" r="7" fill="none" stroke="var(--text)"/><ellipse cx="8" cy="8" rx="3" ry="7" fill="none" stroke="var(--text)"/><path d="M1 8h14" stroke="var(--text)"/></svg>
          <span>www.veltraimportacao.com.br</span>
        </div>
      </div>

      <div class="address-band">Rua xxxxxxxxxxxxxxxxx, numero xx, bairro, cidade, estado, cep</div>

      <div class="edge-line edge-line--bottom"></div>
      <div class="edge-accent" style="left:0;width:60px"></div>
      <div class="edge-accent" style="left:300px;width:120px"></div>
    </section>

    <section class="panel panel--front">
      <div class="backdrop-shape" role="img" aria-label="Forma decorativa escura em segundo plano"></div>
      <div class="brand">
        <div class="brand-dot"></div>
        <span class="brand-name">VELTRA</span>
      </div>
      <div class="edge-line edge-line--bottom"></div>
      <div class="edge-accent" style="left:90px;width:140px"></div>
      <div class="edge-accent" style="left:380px;width:100px"></div>
    </section>
  </div>
</body>
</html>
```